Graphic for Bad Ass Music Business Course
The Best Music Business Course on the Web
Creative Brief
We've launched an online interactive set of videos to teach the music business. It is for aspiring musicians and business professionals that want to learn about the real music business. The product is over 150 videos, transcriptions, quiz questions, and accompanying supplemental video materials. The host/ star of the series was the manager for the rock and roll band GLASSMOTH for 17 years and is a long time executive of the record business. Currently, he is the host of our internet talk show "Tolvar LIVE" where we've had over 100 videos with the most successful people in the music business both artists and professionals. The show is where entertainment, education, mentoring, and the entertainment business collide. We need an official graphic for our course that we can post around social media, post to our website, and embody the attitude, message and spirit of our course. For inspiration, check out our website for the course: www.tolvaracademy-example.com The graphic should communicate that this is "not your typical course". Why is that? Because we take a specific approach to teaching the music business by learning from people who have been there and done that. Going out and trying to make something happen and learning from experienced people in the business is the best way to learn the music business. Imagine being someone who is serious about making a career in the music business seeing this graphic. Or the parent of an aspiring musician. It should inspire you to want to sign up. It should tell you that "wow, this guy really looks like he knows what he's talking about I want to learn more about this course." As you can kind of tell in this creative brief, we work in a fun, loose atmosphere but we always strive to maintain a quality, professional edge. I encourage you to take that same style and try to put it in the graphic! Think: Cold Harbor, the velvet anchors, and Rock and Roll. Title of the Course: Backstage Playbook for the Modern Sound Trade Subtitle: The real music business from a real music business professional somewhere on the page write: with Mark "Tolvar" Dunsby
Entertainment
Aspiring rock stars, aspiring managers of rock bands, people dreaming of doing something big in the music business, guitarists, DJs, Producers... It's a combination of creative people and business people with an entertainment, show-business flare.

```html
<!DOCTYPE html>
<html lang="en">
<head>
<meta charset="utf-8">
<title>The Best Music Business Course on the Web — with Mark "Tolvar" Dunsby</title>
<link rel="stylesheet" href="https://fonts.googleapis.com/css2?family=Bebas+Neue&family=Oswald:wght@400;500&display=swap">
<style>
  :root {
    --sun-yellow: #ffe27a;
    --warm-orange: #ffb06a;
    --hot-pink: #f25bb0;
    --soft-pink: #f7a3cf;
    --violet: #9b54e0;
    --deep-purple: #6a1fb8;
    --headline-purple: #7a2fd0;
    --headline-violet: #8d4fe6;
    --sky-cyan: #8fe3f0;
    --ink: #1a1226;
    --paper: #ffffff;
  }
  * { margin: 0; padding: 0; box-sizing: border-box; }
  html, body { width: 1200px; height: 588px; overflow: hidden; background: var(--paper); }

  .banner {
    position: relative;
    width: 1200px;
    height: 588px;
    overflow: hidden;
    background:
      radial-gradient(ellipse 520px 360px at 120px 80px, var(--sun-yellow) 0%, rgba(255,226,122,0) 75%),
      radial-gradient(ellipse 420px 320px at 300px 560px, var(--sky-cyan) 0%, rgba(143,227,240,0) 70%),
      radial-gradient(ellipse 520px 420px at 620px 260px, var(--soft-pink) 0%, rgba(247,163,207,0) 75%),
      linear-gradient(100deg, var(--warm-orange) 0%, var(--hot-pink) 45%, var(--violet) 75%, var(--deep-purple) 100%);
  }

  .music-decor {
    position: absolute;
    left: 0; top: 40px;
    width: 800px; height: 548px;
  }

  .host-portrait {
    position: absolute;
    right: 0; top: 0;
    width: 470px; height: 588px;
  }

  .host-name {
    position: absolute;
    left: 140px; top: 14px;
    font-family: "Oswald", sans-serif;
    font-weight: 500;
    font-size: 22px;
    letter-spacing: 3px;
    color: var(--ink);
    white-space: nowrap;
  }

  .headline {
    font-family: "Bebas Neue", sans-serif;
    font-weight: 400;
    line-height: 1;
    text-shadow: 2px 2px 0 rgba(255,255,255,.6);
  }
  .headline__line {
    position: absolute;
    display: block;
    white-space: nowrap;
  }
  .headline__top {
    left: 108px; top: 128px;
    font-size: 118px;
    color: var(--headline-violet);
  }
  .headline__middle {
    left: 104px; top: 252px;
    font-size: 112px;
    color: var(--headline-purple);
  }
  .headline__course {
    font-size: 84px;
    color: var(--headline-violet);
  }
  .headline__bottom {
    left: 324px; top: 354px;
    font-size: 96px;
    color: var(--headline-purple);
  }

  .tagline {
    position: absolute;
    left: 12px; top: 500px;
    font-family: "Oswald", sans-serif;
    font-weight: 500;
    font-size: 21px;
    letter-spacing: .5px;
    color: var(--headline-purple);
    text-transform: uppercase;
    transform: rotate(-1.5deg);
    transform-origin: left top;
    white-space: nowrap;
  }
  .tagline__big { font-size: 27px; }
</style>
</head>
<body>
  <main class="banner">
    <svg class="music-decor" viewBox="0 0 800 548" role="img" aria-label="Faint illustration of sheet music staves, notes and a guitar sweeping across the background">
      <defs>
        <linearGradient id="decorFade" x1="0" y1="0" x2="1" y2="1">
          <stop offset="0" stop-color="#ffffff" stop-opacity="0"/>
          <stop offset=".5" stop-color="#ffffff" stop-opacity=".22"/>
          <stop offset="1" stop-color="#ffffff" stop-opacity=".05"/>
        </linearGradient>
      </defs>
      <rect x="0" y="0" width="800" height="548" fill="url(#decorFade)"/>
    </svg>

    <svg class="host-portrait" viewBox="0 0 470 588" role="img" aria-label="Pop-art style portrait of the course host Mark &quot;Tolvar&quot; Dunsby, smiling, in glasses">
      <defs>
        <linearGradient id="portraitTone" x1="0" y1="0" x2="1" y2="1">
          <stop offset="0" stop-color="#f07ac0"/>
          <stop offset=".45" stop-color="#e0a0d8"/>
          <stop offset="1" stop-color="#5a2a8a"/>
        </linearGradient>
        <linearGradient id="portraitEdge" x1="0" y1="0" x2="1" y2="0">
          <stop offset="0" stop-color="#fff" stop-opacity="0"/>
          <stop offset=".18" stop-color="#fff" stop-opacity="1"/>
        </linearGradient>
        <mask id="portraitMask">
          <rect x="0" y="0" width="470" height="588" fill="url(#portraitEdge)"/>
        </mask>
      </defs>
      <rect x="0" y="0" width="470" height="588" fill="url(#portraitTone)" opacity=".9" mask="url(#portraitMask)"/>
    </svg>

    <p class="host-name">MARK "TOLVAR" DUNSBY</p>

    <h1 class="headline">
      <span class="headline__line headline__top">THE BEST</span>
      <span class="headline__line headline__middle">MUSIC BUSINESS <span class="headline__course">COURSE</span></span>
      <span class="headline__line headline__bottom">ON THE WEB</span>
    </h1>

    <p class="tagline"><span class="tagline__big">T</span>he <span class="tagline__big">R</span>eal <span class="tagline__big">M</span>usic <span class="tagline__big">B</span>usiness from <span class="tagline__big">a</span> <span class="tagline__big">R</span>eal <span class="tagline__big">M</span>usic <span class="tagline__big">B</span>usiness <span class="tagline__big">P</span>rofessional</p>
  </main>
</body>
</html>
```